Gutter Cleaning, Power Washing and exterior window washing

I need a flyer made for my business I am starting.
I will be doing gutter cleaning, power washing (Concrete driveways, sidewalks, porches, ect.) and exterior window washing.

I would like the flyer to be on one page. I want the back to be black.

I would like the services I offer to be in bullet points in this order:

Gutter cleaning
Power Washing (Concrete surfaces)
Exterior window washing

I would like the flyer to not be super 'busy' and distracting. A good simple design thats not too boring but again, not too busy.

I would like the colors to be a mix of:

Black
Turquoise

Somewhere on the flyer I would like it to say something like "Call or text Morgan Pellicott to schedule...." you can make something up but it needs to say something like that on there.

I don't want generic pictures of power washing or window cleaning or gutter cleaning, please.

Target Market(s)

Residential Customers

Industry/Entity Type

Business

Font styles to use
Sans Serif

Colors
000000
0592cd

Requirements
Must have
• Gutter cleaning
• Power Washing (Concrete surfaces)
• Exterior window washing
• all in bullet points in this order
Nice to have
• Cool modern design
Should not have
• Generic pictures

```html
<!DOCTYPE html>
<html lang="en">
<head>
<meta charset="utf-8">
<title>Cleaning Services Flyer</title>
<link href="https://fonts.googleapis.com/css2?family=Montserrat:wght@700;800&family=Roboto:wght@300;400;500;700&display=swap" rel="stylesheet">
<style>
  :root {
    --canvas: #b3b3b3;
    --turquoise: #0592cd;
    --turquoise-light: #56cdf7;
    --black: #000000;
    --ink: #1d1d1d;
    --white: #ffffff;
    --muted: #d0d0d0;
  }
  * { box-sizing: border-box; margin: 0; padding: 0; }
  html, body {
    width: 1014px; height: 1200px; overflow: hidden;
    background: var(--canvas);
    font-family: "Roboto", sans-serif;
  }
  .sheet {
    position: absolute; top: 291px; width: 440px; height: 618px;
    overflow: hidden; box-shadow: 0 3px 8px rgba(0,0,0,.35);
  }
  .front {
    left: 44px;
    background: radial-gradient(circle at 35% 5%, var(--turquoise-light) 0%, #2cb4ea 35%, var(--turquoise) 100%);
  }
  .back {
    left: 530px;
    background: linear-gradient(90deg, #1b1b1b 0%, #333 55%, #1e1e1e 100%);
  }
  .headline-frame {
    position: absolute; left: 45px; top: 45px; width: 350px; height: 93px;
    border: 1.5px solid var(--ink);
  }
  .brand-name {
    position: absolute; left: 50%; top: -11px; transform: translateX(-50%);
    padding: 0 6px; background: #48c5f3;
    font-family: "Roboto", sans-serif; font-weight: 500; font-size: 19px;
    color: var(--white); white-space: nowrap; line-height: 20px;
  }
  .headline-top {
    position: absolute; left: 0; right: 0; top: 16px; text-align: center;
    font-weight: 300; font-size: 29px; letter-spacing: 0.5px; color: var(--white);
  }
  .headline-main {
    position: absolute; left: 0; right: 0; top: 46px; text-align: center;
    font-family: "Montserrat", sans-serif; font-weight: 800; font-size: 34px;
    letter-spacing: 0.5px; color: var(--white);
  }
  .worker-photo {
    position: absolute; left: 250px; top: 142px; width: 186px; height: 382px;
    background: linear-gradient(180deg, rgba(40,60,160,.55) 0%, rgba(30,50,170,.65) 55%, rgba(60,90,140,.55) 100%);
    border-radius: 40px 40px 8px 8px;
  }
  .services { position: absolute; left: 45px; top: 0; list-style: none; }
  .service {
    position: absolute; left: 0; display: flex; align-items: center; width: 260px;
  }
  .service-icon {
    width: 68px; height: 68px; border-radius: 50%; flex: none;
    background: radial-gradient(circle at 40% 35%, #3a3a3a, #111 70%);
    border: 3px solid #c9c9c9; box-shadow: 0 0 0 1px #333;
    display: flex; align-items: center; justify-content: center;
  }
  .service-label {
    margin-left: 10px; color: var(--white); font-weight: 500;
    font-size: 18px; line-height: 21px; text-transform: uppercase;
  }
  .service-note { display: block; font-weight: 400; font-size: 12px; line-height: 13px; text-transform: none; }
  .service.gutter { top: 178px; }
  .service.power { top: 319px; }
  .service.window { top: 461px; }
  .footer-band {
    position: absolute; left: 0; bottom: 0; width: 100%; height: 52px;
    background: linear-gradient(180deg, #2a2a2a, #111);
  }
  .call-tab {
    position: absolute; right: 0; bottom: 0; width: 214px; height: 89px;
    background: linear-gradient(180deg, #2a2a2a, #111);
    clip-path: polygon(22% 0, 100% 0, 100% 100%, 0 100%, 0 42%, 12% 42%);
  }
  .call-block { position: absolute; left: 255px; top: 538px; color: var(--white); }
  .call-title { font-weight: 500; font-size: 19px; line-height: 20px; }
  .call-sub { font-size: 11px; line-height: 13px; color: var(--muted); }
  .call-phone { font-weight: 500; font-size: 26px; line-height: 32px; letter-spacing: 0.3px; white-space: nowrap; }
  .contact {
    position: absolute; top: 580px; color: var(--white);
    font-size: 7.5px; line-height: 11px; white-space: nowrap;
  }
  .contact-line { display: flex; align-items: center; gap: 3px; }
  .contact.online { left: 18px; }
  .contact.address { left: 150px; }
</style>
</head>
<body>
  <section class="sheet front" aria-label="Flyer front">
    <div class="headline-frame">
      <span class="brand-name">YOUR LOGO</span>
      <p class="headline-top">IF YOU WANT IT CLEAN</p>
      <p class="headline-main">CALL OUR TEAM</p>
    </div>

    <div class="worker-photo" role="img" aria-label="Smiling cleaner in blue apron and gloves leaning on a mop"></div>

    <ul class="services">
      <li class="service gutter">
        <span class="service-icon">
          <svg width="38" height="34" viewBox="0 0 38 34" aria-hidden="true">
            <path d="M2 4 H36 V10 Q36 14 32 14 H24 V30 H16 V20 L22 14 H6 Q2 14 2 10 Z" fill="#fff"/>
          </svg>
        </span>
        <span class="service-label">Gutter<br>Cleaning</span>
      </li>
      <li class="service power">
        <span class="service-icon">
          <svg width="40" height="34" viewBox="0 0 40 34" aria-hidden="true">
            <path d="M4 28 Q10 14 20 16 L26 13" stroke="#fff" stroke-width="2.5" fill="none"/>
            <rect x="24" y="10" width="6" height="6" fill="#fff"/>
            <circle cx="33" cy="9" r="1.2" fill="#fff"/><circle cx="36" cy="12" r="1.2" fill="#fff"/>
            <circle cx="33" cy="15" r="1.2" fill="#fff"/><circle cx="37" cy="17" r="1.2" fill="#fff"/>
          </svg>
        </span>
        <span class="service-label">Power<br>Washing<span class="service-note">(Concrete surfaces)</span></span>
      </li>
      <li class="service window">
        <span class="service-icon">
          <svg width="38" height="36" viewBox="0 0 38 36" aria-hidden="true">
            <rect x="6" y="14" width="22" height="18" fill="none" stroke="#fff" stroke-width="2.5"/>
            <line x1="17" y1="14" x2="17" y2="32" stroke="#fff" stroke-width="2"/>
            <line x1="22" y1="10" x2="32" y2="2" stroke="#fff" stroke-width="2.5"/>
            <rect x="27" y="0" width="10" height="4" transform="rotate(-38 32 2)" fill="#fff"/>
          </svg>
        </span>
        <span class="service-label">Terior<br>Window<br>Washing</span>
      </li>
    </ul>

    <div class="footer-band"></div>
    <div class="call-tab"></div>
    <div class="call-block">
      <p class="call-title">CALL OR TEXT</p>
      <p class="call-sub">Morgan Pellicott to schedule</p>
      <p class="call-phone">321-555-0148</p>
    </div>

    <div class="contact online">
      <p class="contact-line">
        <svg width="7" height="5" viewBox="0 0 7 5" aria-hidden="true"><rect width="7" height="5" fill="#0592cd"/><path d="M0 0 L3.5 3 L7 0" stroke="#fff" stroke-width=".8" fill="none"/></svg>
        hello@brightedgeclean.com
      </p>
      <p class="contact-line">
        <svg width="7" height="7" viewBox="0 0 7 7" aria-hidden="true"><circle cx="3.5" cy="3.5" r="3.5" fill="#0592cd"/></svg>
        www.brightedgeclean.com
      </p>
    </div>
    <div class="contact address">
      <p class="contact-line">
        <svg width="6" height="8" viewBox="0 0 6 8" aria-hidden="true"><path d="M3 8 L0.4 4 A3 3 0 1 1 5.6 4 Z" fill="#0592cd"/><circle cx="3" cy="3" r="1" fill="#111"/></svg>
        48 Harbor Ln. Coral Bay,
      </p>
      <p class="contact-line" style="padding-left:9px">FL 32900</p>
    </div>
  </section>

  <section class="sheet back" aria-label="Flyer back"></section>
</body>
</html>
```